Online medical reviews website needs banner advert!

We need banner advert templates for our website, www.wardplume.com. These should meet the technical requirements of our partner (uploaded).

Our groundbreaking website allows doctors in training to rate and review their training.

The adverts should use the same modern design language and colour scheme as our website. They should use the text 'Help a junior doctor make a big decision - rate your training!'.

Vector assets should be supplied, allowing us to use alternative text in future.
Updates

Industry/Entity Type

Healthcare

Font styles to use
Other font styles liked:
• Karla

Colors
3277b5
0555a3
ffffff

Requirements
Must have
• Similar design to our website. Should be elegant & modern. Must allow future text to be easily inserted.
Should not have
• Unrelated design.

```html
<!DOCTYPE html>
<html lang="en">
<head>
<meta charset="utf-8">
<title>Ward Plume – Banner Advert</title>
<link href="https://fonts.googleapis.com/css2?family=Oswald:wght@500;700&family=Archivo+Black&family=Lato:wght@400&display=swap" rel="stylesheet">
<style>
  :root {
    --navy: #0a2a87;
    --charcoal: #3b3b3b;
    --ink: #1a1a1a;
    --paper: #ffffff;
    --page: #ffffff;
    --coat: #e9ebef;
    --coat-shade: #c9ccd3;
    --skin: #e8c3a6;
    --hair: #7a5a45;
  }
  * { margin: 0; padding: 0; box-sizing: border-box; }
  html, body {
    width: 1200px; height: 797px; overflow: hidden;
    background: var(--page);
  }
  .banner {
    position: absolute; left: 112px; top: 116px;
    width: 976px; height: 548px;
    background: var(--paper);
    overflow: hidden;
  }
  .banner__shapes { position: absolute; inset: 0; }
  .headline {
    position: absolute; left: 24px; top: 52px;
    line-height: 1;
  }
  .headline__lead {
    display: block;
    font-family: "Oswald", sans-serif; font-weight: 700;
    font-size: 38px; letter-spacing: 0.6px;
    color: var(--navy);
    transform: scaleX(1.035); transform-origin: left;
  }
  .headline__main {
    display: block; margin-top: -2px;
    font-family: "Archivo Black", sans-serif;
    font-size: 42px; letter-spacing: 0.5px;
    color: var(--charcoal);
  }
  .copy {
    position: absolute; left: 26px; width: 398px;
    font-family: "Lato", sans-serif; font-size: 13px; line-height: 16px;
    color: var(--ink); text-align: justify;
  }
  .copy--intro { top: 162px; }
  .copy--scores { top: 242px; }
  .subhead {
    position: absolute; left: 24px; top: 216px;
    font-family: "Oswald", sans-serif; font-weight: 500;
    font-size: 19px; color: var(--navy);
  }
  .guide {
    position: absolute; left: 24px; top: 322px;
    font-family: "Oswald", sans-serif; font-weight: 500;
    font-size: 19px; line-height: 24px; letter-spacing: 0.4px;
    color: var(--navy);
  }
  .cta {
    position: absolute; left: 23px; top: 413px;
    font-family: "Oswald", sans-serif; font-weight: 700;
    font-size: 42px; line-height: 1;
  }
  .cta__label { color: var(--navy); }
  .cta__number { color: var(--charcoal); font-weight: 500; }
  .brand {
    position: absolute; left: 562px; top: 56px;
    display: flex; align-items: center; gap: 16px;
    font-family: "Lato", sans-serif; font-weight: 400;
    font-size: 54px; letter-spacing: -0.5px; line-height: 1;
    color: var(--navy);
  }
  .brand__mark {
    width: 26px; height: 26px;
    background: var(--navy);
    margin-top: -22px;
  }
</style>
</head>
<body>
  <div class="banner">
    <svg class="banner__shapes" width="976" height="548" viewBox="0 0 976 548">
      <defs>
        <linearGradient id="photoBase" x1="0" y1="0" x2="0" y2="1">
          <stop offset="0" stop-color="#ffffff"/>
          <stop offset="0.4" stop-color="#f7f6f5"/>
          <stop offset="1" stop-color="#e4e6ea"/>
        </linearGradient>
        <radialGradient id="photoWarm" cx="0.55" cy="0.45" r="0.5">
          <stop offset="0" stop-color="var(--skin)" stop-opacity="0.55"/>
          <stop offset="0.5" stop-color="var(--hair)" stop-opacity="0.12"/>
          <stop offset="1" stop-color="var(--hair)" stop-opacity="0"/>
        </radialGradient>
        <linearGradient id="photoCoats" x1="0" y1="0" x2="0" y2="1">
          <stop offset="0" stop-color="var(--coat)" stop-opacity="0"/>
          <stop offset="0.55" stop-color="var(--coat)" stop-opacity="0.9"/>
          <stop offset="1" stop-color="var(--coat-shade)" stop-opacity="1"/>
        </linearGradient>
        <clipPath id="photoClip">
          <path d="M612,0 H976 V548 H416 C430,535 450,510 470,470 C510,400 490,260 498,150 C505,70 560,20 612,0 Z"/>
        </clipPath>
      </defs>
      <path class="swoosh swoosh--charcoal" fill="#3b3b3b"
            d="M508,0 C470,30 455,90 456,150 C458,260 465,400 420,490 C410,505 405,510 396,514 H0 V548 H976 V0 Z"/>
      <path class="swoosh swoosh--gap" fill="#ffffff"
            d="M576,0 C520,25 478,80 472,150 C466,260 485,400 440,480 C420,515 395,535 360,548 H976 V0 Z"/>
      <path class="swoosh swoosh--navy" fill="#0a2a87"
            d="M586,0 C532,25 488,80 482,150 C475,260 495,400 455,475 C435,510 410,535 380,548 H976 V0 Z"/>
      <g class="photo" clip-path="url(#photoClip)" role="img"
         aria-label="Photo of a group of smiling junior doctors in white coats with stethoscopes, one holding a clipboard">
        <rect x="400" y="0" width="576" height="548" fill="url(#photoBase)"/>
        <rect x="400" y="130" width="576" height="418" fill="url(#photoWarm)"/>
        <rect x="400" y="260" width="576" height="288" fill="url(#photoCoats)"/>
      </g>
    </svg>

    <h1 class="headline">
      <span class="headline__lead">WOULD YOU RECOMMEND</span>
      <span class="headline__main">YOUR TRAINING?</span>
    </h1>

    <p class="copy copy--intro">We want our reviews to be as useful as possible – both for junior doctors, but also for organisations that want to<br>improve their training.</p>

    <h2 class="subhead">Our scores</h2>
    <p class="copy copy--scores">We know that everyone has a different idea about what constitutes great training. With that in mind, we’d encourage you to provide as much detail as possible in your comments, so other junior doctors can make better decisions about where they train.</p>

    <p class="guide">We use the following as a rough guide to help<br>us award numerical ratings<br>it might help you too!</p>

    <p class="cta"><span class="cta__label">CALL NOW</span> <span class="cta__number">0123456789</span></p>

    <div class="brand"><span class="brand__name">Ward Plume</span><span class="brand__mark"></span></div>
  </div>
</body>
</html>
```